Redcliff Oil & Gas Exploration, LLC

Our website (www.redcliffoilandgas.example) is poorly done and dated. I want to redo it with one main page and wide format photos or oil & gas drilling and production. Perhaps all of the pages listed on the left side of the existing site could be viewed by scrolling down further on the new main page. I want something clean and easy to navigate.

Target Market(s)

Other oil and gas companies and people that we have contacted regarding selling or leasing their mineral rights. These people will come to our website to research our company and become more comfortable doing business with us.

Industry/Entity Type

Oil And Gas

Coding

Coded - Design and coding required

Number of Pages Required

1 page

Font styles to use
Serif

Requirements
Must have
• Clean and uncluttered. Nice, clear wide format picture or oil well or rig and landscape.

```html
<!DOCTYPE html>
<html lang="en">
<head>
<meta charset="utf-8">
<title>Redcliff Oil &amp; Gas Exploration, LLC</title>
<link rel="stylesheet" href="https://fonts.googleapis.com/css2?family=Open+Sans:wght@400;600;700&display=swap">
<style>
:root{
  --orange:#f0931f;
  --ink:#333333;
  --text:#6d6d6d;
  --light:#f0f0f0;
  --white:#ffffff;
  --footer:#3a3a3a;
  --footer-dark:#262626;
}
*{box-sizing:border-box;margin:0;padding:0}
html,body{width:1200px;height:4215px;overflow:hidden}
body{font-family:'Open Sans',Arial,sans-serif;color:var(--text);background:var(--white);position:relative}
.abs{position:absolute}

/* hero */
.hero{top:0;left:0;width:1200px;height:800px;
  background:linear-gradient(180deg,#27272b 0%,#4a3f37 38%,#a9682a 62%,#d98a2c 70%,#3b2b1f 86%,#1d1814 100%)}
.hero-shade{top:0;left:0;width:1200px;height:800px;background:rgba(0,0,0,.25)}
.top-email{top:86px;left:52px;color:var(--white);font-size:15px}
.brand{top:40px;left:0;width:1200px;text-align:center;color:var(--orange);font-weight:700;font-size:22px;line-height:30px}
.brand-dot{display:inline-block;width:18px;height:18px;border-radius:50%;background:var(--orange);vertical-align:-2px;margin-right:10px}
.top-call{top:86px;right:52px;color:var(--white);font-size:15px}
.top-call b{color:var(--orange);font-weight:600;font-size:17px}
.hero-title{top:305px;left:150px;width:900px;text-align:center;color:var(--white);font-size:36px;line-height:48px;font-weight:600;text-transform:uppercase}
.hero-title span{color:var(--orange)}
.hero-text{top:505px;left:190px;width:820px;text-align:center;color:var(--white);font-size:15px;line-height:24px}
.stat{top:685px;width:300px;text-align:center;color:var(--white);font-size:14px;line-height:19px}
.stat strong{display:block;color:var(--orange);font-size:40px;line-height:48px;font-weight:700}

/* story */
.story{top:800px;left:0;width:1200px;height:585px;background:var(--light)}
.story-photo{top:43px;width:380px;height:185px}
.photo-pump{left:145px;background:linear-gradient(180deg,#4d9ee6 0%,#9fcff5 55%,#d8d4cc 100%)}
.photo-barrels{left:652px;background:linear-gradient(180deg,#3f8fd0 0%,#2f6fb0 50%,#3aa38a 100%)}
.story-col{top:330px;width:390px;text-align:center}
.story-col h2{color:var(--ink);font-size:19px;font-weight:700;margin-bottom:12px}
.story-col p{font-size:14.5px;line-height:22px}
.story-col b{color:var(--ink);font-weight:600}

/* team */
.member-photo{height:305px}
.photo-grey{background:linear-gradient(120deg,#cfcfcf,#8e8e8e)}
.photo-warm{background:linear-gradient(120deg,#e6e2dd,#b89a6a)}
.photo-cool{background:linear-gradient(120deg,#e8e8e8,#b9c0c7)}
.member h3{color:var(--ink);font-size:25px;font-weight:600;line-height:32px}
.member .lead{color:var(--ink);font-size:15.5px;line-height:22px;margin-top:6px}
.member p{font-size:14.5px;line-height:21px;margin-top:22px}

/* areas */
.areas{top:2614px;left:0;width:1200px;height:1306px;background:var(--light)}
.map{left:126px;width:680px;height:548px;background:linear-gradient(135deg,#ffffff,#e4e4e4);border:2px solid #bdbdbd}
.area-title{left:835px;color:var(--ink);font-size:27px;line-height:36px}

/* footer */
.footer{top:3920px;left:0;width:1200px;height:240px;background:var(--footer);color:#e6e6e6}
.footer h4{position:absolute;top:55px;left:50px;color:var(--orange);font-size:19px;font-weight:600}
.office{top:90px;font-size:13px;line-height:17px}
.office .tag{color:var(--orange)}
.copyright{top:4160px;left:0;width:1200px;height:55px;background:var(--footer-dark);color:#cfcfcf;font-size:13px;text-align:center;line-height:55px}
</style>
</head>
<body>

<section class="hero abs" role="img" aria-label="Wide photograph of oil pumpjacks silhouetted against a sunset sky"></section>
<div class="hero-shade abs"></div>
<div class="top-email abs">inquiry@redcliffoilandgas.example</div>
<div class="brand abs"><span class="brand-dot"></span>Redcliff Oil &amp; Gas Exploration, LLC</div>
<div class="top-call abs">call us &nbsp;<b>405.555.0142</b></div>
<h1 class="hero-title abs"><span>Redcliff</span> is actively leasing and purchasing mineral rights in Texas, Oklahoma and Kansas.</h1>
<p class="hero-text abs">In Texas our area of focus is the East Texas Basin. In Oklahoma we are active across the state with emphasis on the SCOOP and the Mississippian Plays. Redcliff is dedicated to expanding our asset base, targeting oil prone plays, and continuing to acquire minerals and prospective leasehold.</p>
<div class="stat abs" style="left:145px"><strong>25,000</strong>net acres of leasehold in<br>Texas, Oklahoma and Kansas</div>
<div class="stat abs" style="left:720px"><strong>10,000</strong>mineral acres<br>primarily in Oklahoma</div>

<section class="story abs">
  <div class="story-photo photo-pump abs" role="img" aria-label="Photograph of an oil pumpjack under a blue sky"></div>
  <div class="story-photo photo-barrels abs" role="img" aria-label="Photograph of rows of blue and green oil barrels"></div>
  <div class="story-col abs" style="left:130px">
    <h2>OUR STORY</h2>
    <p>Redcliff Oil &amp; Gas Exploration, LLC was founded in 2011 by <b>Kevin Halvorsen</b>. In 2012 <b>David Halvorsen</b> &amp; <b>Charles Halvorsen</b> joined the company. In 2013, <b>Chad Morrow</b> joined the company as a Petroleum Engineer and in 2015, became a partner. Redcliff has expanded their business, and currently has offices located in Fort Worth and Oklahoma City.</p>
  </div>
  <div class="story-col abs" style="left:650px">
    <h2>OUR ACTIVITIES</h2>
    <p>Since 2012 Redcliff has acquired more than 25,000 net acres of leasehold in Texas, Oklahoma and Kansas. During the same time, the company has also purchased in excess of 10,000 mineral acres primarily in Oklahoma and to a lesser extent, East Texas. In addition, Redcliff has participated in hundreds of wells with top tier operators.</p>
  </div>
</section>

<article class="member">
  <div class="member-photo photo-grey abs" style="top:1385px;left:0;width:455px" role="img" aria-label="Photograph of a geologist working at a desk"></div>
  <div class="abs" style="top:1428px;left:534px;width:620px">
    <h3>About Charles Halvorsen</h3>
    <div class="lead">Charlie has over 35 years of experience as a petroleum geologist.</div>
    <p>He was most recently the East Texas Exploration Manager at Crestline Energy for the past nine years. He left Crestline in April 2012 to join Redcliff. Charlie's focus at Redcliff is prospecting in East Texas. Charlie attended Blue Ridge State University and the University of the Delta where he received a Bachelor's and Master's degree in geology.</p>
  </div>
</article>

<article class="member">
  <div class="abs" style="top:1735px;left:52px;width:640px">
    <h3>About Kevin Halvorsen</h3>
    <div class="lead">Kevin has been an independent landman since 2005.</div>
    <p>Since starting Redcliff, he has successfully put together and sold multiple lease packages in the Haynesville, Woodford, and Niobrara plays, among many others. His current focus is purchasing minerals in Oklahoma, particularly in the SCOOP and Mississippian plays.</p>
  </div>
  <div class="member-photo photo-warm abs" style="top:1692px;left:739px;width:461px" role="img" aria-label="Photograph of a landman in a hard hat on a work site"></div>
</article>

<article class="member">
  <div class="member-photo photo-grey abs" style="top:2000px;left:0;width:464px" role="img" aria-label="Photograph of a man in a hard hat and sunglasses at a facility"></div>
  <div class="abs" style="top:2062px;left:534px;width:620px">
    <h3>About David Halvorsen</h3>
    <div class="lead">David spent seven years at Crestline Energy, managing commercial real estate transactions</div>
    <p>He left in January of 2012 to join Kevin in expanding Redcliff. He has since managed and sold several East Texas prospects. David oversees leasing prospects and purchasing minerals in East Texas. David received his Bachelor's degree in Management from Gulf Coast State University.</p>
  </div>
</article>

<article class="member">
  <div class="abs" style="top:2330px;left:52px;width:655px">
    <h3>About Chad Morrow</h3>
    <p style="margin-top:10px">Previously, Chad spent six years at Bluestem Energy, Inc., where he worked as a completion engineer, production engineer and reservoir engineer. Being able to work in all three engineering departments allowed him to broaden his knowledge of the petroleum industry as a whole. He has evaluated mineral and non-operated working interest deals that have been generated through Redcliff's land group. His evaluation process includes decline curve analysis, PV10 calculations and future cash flow modeling. Chad holds a Bachelor's degree in Petroleum Engineering from High Plains Technical University. He is currently a member of Prairie Independent Petroleum Association and Guild of Reservoir Engineers.</p>
  </div>
  <div class="member-photo photo-cool abs" style="top:2305px;left:753px;width:447px" role="img" aria-label="Photograph of an engineer standing in an office"></div>
</article>

<section class="areas abs">
  <div class="map abs" style="top:84px" role="img" aria-label="County map of East Texas with prospect areas marked in orange"></div>
  <div class="area-title abs" style="top:140px">Texas<br>Areas of Interest</div>
  <div class="map abs" style="top:674px" role="img" aria-label="County map of Oklahoma areas of interest with prospects marked in orange"></div>
  <div class="area-title abs" style="top:705px">Oklahoma<br>Areas of Interest</div>
</section>

<footer class="footer abs">
  <h4>CONTACT US</h4>
  <div class="office abs" style="left:50px">Fort Worth Office<br>840 Ledger Street<br>Suite 210<br>Fort Worth, Texas 76102</div>
  <div class="office abs" style="left:236px">Oklahoma City Office<br>77 Prairie Avenue<br>Suite 5<br>Oklahoma City, Oklahoma 73102</div>
  <div class="office abs" style="left:472px"><span class="tag">Land</span><br>Oklahoma City Office<br>Kevin Halvorsen<br>405.555.0178<br>kevin@redcliffoilandgas.example</div>
  <div class="office abs" style="left:708px"><br>Fort Worth Office<br>David Halvorsen<br>817.555.0193<br>david@redcliffoilandgas.example</div>
  <div class="office abs" style="left:941px"><span class="tag">Geology</span><br>Fort Worth Office<br>Charles Halvorsen<br>817.555.0194<br>charles@redcliffoilandgas.example</div>
</footer>
<div class="copyright abs">Content copyright 2017. &nbsp;All rights reserved.</div>

</body>
</html>
```